International Travel Technology R&D business needs a wordpress website

We are a start up team of initially 2 individuals but plan to grow our team quickly, we have deep experience in travel technology. Our goal is to provide next generation technology research and development on behalf of our clients who are leading players in the travel technology industry. Attached our logos.

Target Market(s)

Travel Technology companies

Industry/Entity Type

Travel Industry

Coding

Coded - Design and coding required

Font styles to use
Sans Serif

Requirements
Must have
• Make use of our logo and colour scheme in the attached. Has to have a sense of adventure/ stepping into the unknown but equally must convey a sense of professionalism , we are a safe pair of hands. Sample themes are in the attachment .
Nice to have
• We have identified a theme on layoutgrove which we feel would be inspirational. We hahe attached them to help in the design as inspiration.
Should not have
• images of airplanes , hotels etc, we want to project a future image.

```html
<!DOCTYPE html>
<html lang="en">
<head>
<meta charset="utf-8">
<title>Wayfront Technology Labs</title>
<link href="https://fonts.googleapis.com/css2?family=Oswald:wght@400;500&family=Open+Sans:wght@400;600&family=Raleway:wght@400;600&display=swap" rel="stylesheet">
<style>
:root{
  --navy:#1f2f7a;
  --blue:#2c4aa6;
  --sky:#5b8fd0;
  --green:#5aa43a;
  --green-dark:#3f7a2c;
  --ink:#222;
  --grey:#777;
  --light:#eef2f7;
  --panel:#2b2d31;
  --deep:#0f1d4a;
  --white:#fff;
}
*{margin:0;padding:0;box-sizing:border-box}
html,body{width:1200px;height:3814px;overflow:hidden}
body{font-family:"Open Sans",sans-serif;color:var(--ink);background:var(--white);position:relative}
.wrap{width:1000px;margin:0 auto;position:relative}
h2,h3,.oswald{font-family:"Oswald",sans-serif;font-weight:400}

/* header */
.site-header{height:114px;display:flex;align-items:center;justify-content:space-between;padding:0 100px}
.brand{font-family:"Oswald",sans-serif;font-weight:500;font-size:30px;color:var(--navy);letter-spacing:2px;display:flex;align-items:center;gap:12px}
.brand-dot{width:22px;height:22px;border-radius:50%;background:var(--green)}
.main-nav{display:flex;gap:34px;font-family:"Oswald",sans-serif;font-size:13px;color:#555;text-transform:uppercase}
.main-nav .active{color:var(--blue)}

/* hero */
.hero{height:547px;position:relative;background:linear-gradient(120deg,#4a5a66 0%,#2f3b48 40%,#8a98a6 75%,#c9d2da 100%)}
.hero-text{position:absolute;left:122px;top:200px;color:var(--white)}
.hero-text h1{font-family:"Oswald",sans-serif;font-weight:500;font-size:44px;letter-spacing:1px}
.hero-text p{font-family:"Raleway",sans-serif;font-size:19px;line-height:32px;margin-top:8px;font-weight:600}
.hero-arrow{position:absolute;top:258px;width:36px;height:36px;border:2px solid rgba(255,255,255,.7);border-radius:50%}
.hero-arrow.prev{left:36px}.hero-arrow.next{right:36px}

/* welcome */
.welcome{height:369px;position:relative}
.welcome-photo{position:absolute;left:100px;top:-51px;width:345px;height:370px;background:linear-gradient(160deg,#7c8f54,#3d5a2c 60%,#a8a37a);box-shadow:0 4px 14px rgba(0,0,0,.35)}
.welcome-body{position:absolute;left:503px;top:50px;width:560px}
.welcome-body h2{font-size:34px;color:var(--ink);line-height:40px}
.welcome-body h3{font-size:24px;color:var(--blue);line-height:30px}
.welcome-body p{font-size:12.5px;line-height:22px;color:var(--grey);margin-top:30px}
.btn{display:inline-block;background:var(--green);color:var(--white);font-size:13px;padding:11px 26px;margin-top:26px;border-radius:2px}

/* features */
.features{height:622px;background:linear-gradient(135deg,#f3f5fb,#e9eef6 50%,#f6eef2);position:relative;padding-top:52px}
.section-title{text-align:center;font-family:"Oswald",sans-serif;font-size:30px}
.section-sub{text-align:center;font-size:13px;color:var(--grey);margin-top:4px}
.feature-grid{display:grid;grid-template-columns:1fr 1fr;column-gap:40px;row-gap:58px;margin-top:56px}
.feature{display:flex;gap:24px}
.feature-icon{flex:none;width:56px;height:56px;border-radius:50%;background:var(--white);border:1px solid #ddd;display:flex;align-items:center;justify-content:center}
.feature h4{font-family:"Oswald",sans-serif;font-weight:400;font-size:17px;letter-spacing:.5px}
.feature p{font-size:11.5px;line-height:19px;color:var(--grey);margin-top:8px;width:390px}
.feature a{display:block;font-size:12px;color:var(--ink);margin-top:12px}

/* stats */
.stats{position:absolute;left:100px;top:521px;width:1000px;height:356px;display:grid;grid-template-columns:330px 335px 335px;color:var(--white);z-index:2}
.stats-col{background:var(--panel);display:flex;flex-direction:column;justify-content:space-around;padding:30px 0}
.stat{display:flex;align-items:center;gap:26px;padding:0 40px}
.stat.right{justify-content:flex-end}
.stat-icon{width:64px;height:64px;border-radius:50%;border:1px solid rgba(255,255,255,.25);display:flex;align-items:center;justify-content:center}
.stat b{display:block;font-family:"Oswald",sans-serif;font-weight:500;font-size:32px}
.stat span{font-size:15px}
.video-col{background:linear-gradient(160deg,#4f8a3e,#2f5a28);display:flex;flex-direction:column;align-items:center;padding-top:96px;text-align:center}
.play{width:80px;height:80px;border-radius:50%;border:2px solid rgba(255,255,255,.8);display:flex;align-items:center;justify-content:center}
.video-col h3{font-size:22px;margin-top:40px}
.video-col p{font-size:14px;line-height:22px;margin-top:6px;width:240px}

/* projects */
.projects{padding-top:290px;height:838px}
.projects .section-title span{color:var(--blue)}
.project-grid{display:grid;grid-template-columns:203px 203px 203px 320px;column-gap:23px;margin-top:44px;position:relative}
.project-thumb{height:132px}
.project p{font-size:15px;line-height:26px;margin-top:12px;height:84px}
.project-feature{grid-column:4;grid-row:1/3}
.project-feature .project-thumb{height:204px}
.project-feature .date{font-size:13px;color:var(--grey);margin-top:18px}
.project-feature h4{font-family:"Raleway",sans-serif;font-weight:600;font-size:23px;line-height:28px;margin-top:6px}
.project-feature p{font-size:10.5px;line-height:17px;color:var(--grey);height:auto;margin-top:12px}

/* testimonials */
.testimonials{height:389px;background:linear-gradient(90deg,#4f7fc4,#6e9bd6);color:var(--white);padding-top:44px}
.testi-head{display:flex;justify-content:space-between;align-items:center}
.testi-head h2{font-size:28px}
.testi-head h2 span{color:var(--navy)}
.testi-nav{display:flex;gap:4px}
.testi-nav i{width:20px;height:20px;border-radius:50%;background:rgba(255,255,255,.8);display:block}
.testi-label{font-size:14px;margin-top:6px}
.testi-grid{display:grid;grid-template-columns:1fr 1fr;gap:40px;margin-top:58px}
.testi-top{display:flex;align-items:center;gap:30px;padding-left:4px}
.avatar{width:92px;height:92px;border-radius:50%;border:3px solid var(--white);background:linear-gradient(160deg,#c99a7a,#6b4a3a)}
.testi-top b{font-family:"Oswald",sans-serif;font-weight:400;font-size:18px;display:block}
.testi-top span{font-size:13px}
.testi p{font-size:11.5px;line-height:20px;margin-top:16px}

/* blog */
.blog{height:445px;padding-top:44px}
.blog-grid{display:grid;grid-template-columns:repeat(4,236px);gap:18px;margin-top:40px}
.post{text-align:center;box-shadow:0 1px 4px rgba(0,0,0,.12);padding-bottom:24px}
.post-thumb{height:140px}
.post h4{font-family:"Raleway",sans-serif;font-weight:600;font-size:15px;margin-top:26px;padding-bottom:12px;border-bottom:2px solid var(--sky);display:inline-block}
.post p{font-size:11.5px;line-height:19px;color:var(--grey);margin-top:12px;padding:0 28px}

/* contact */
.contact{height:425px;background:linear-gradient(180deg,#1a2a66,var(--deep));color:var(--white);padding-top:48px}
.contact .section-sub{color:#c9d2ea;width:560px;margin:14px auto 0;line-height:20px;font-size:12px}
.contact-body{display:flex;margin-top:40px}
.contact-info{width:332px;font-size:12px}
.contact-info h4{font-weight:400;font-size:15px;margin-bottom:16px}
.contact-info li{list-style:none;display:flex;gap:14px;align-items:center;margin-bottom:14px;color:#c9d2ea}
.socials{display:flex;gap:10px;margin-top:28px}
.socials i{width:24px;height:24px;border-radius:50%;border:1px solid #8a96c0;display:block}
.contact-form{flex:1;font-size:13px}
.form-row{display:flex;gap:30px}
.field{flex:1;border-bottom:1px solid #5a6aa0;padding-bottom:24px;margin-bottom:24px}
.field.message{height:116px}
.submit{display:inline-block;background:var(--green);font-size:12px;padding:8px 18px;border-radius:2px}

.site-footer{height:64px;background:var(--green);color:var(--white);font-size:13px;display:flex;align-items:center;justify-content:center}
</style>
</head>
<body>

<header class="site-header">
  <div class="brand"><span class="brand-dot"></span>WAYFRONT TECH LABS</div>
  <nav class="main-nav">
    <span class="active">Home</span><span>About Us</span><span>Features</span><span>Blog</span><span>Projects</span><span>Testimonial</span><span>Contact Us</span>
  </nav>
</header>

<section class="hero" role="img" aria-label="Photo of business people shaking hands in a bright office">
  <span class="hero-arrow prev"></span><span class="hero-arrow next"></span>
  <div class="hero-text">
    <h1>WAYFRONT TECHNOLOGY LABS</h1>
    <p>Our goal is to provide next generation technology research<br>and development on behalf of our clients</p>
  </div>
</section>

<section class="welcome">
  <div class="welcome-photo" role="img" aria-label="Photo of a traveller in a hat working on a tablet outdoors"></div>
  <div class="welcome-body">
    <h2>WELCOME TO</h2>
    <h3>WAYFRONT TECHNOLOGY LABS</h3>
    <p>It is a long established fact that a reader will be distracted by the readable content of a page when looking at its layout. The point of using Lorem Ipsum is that it has a more-or-less normal distribution of letters, as opposed to using Content here, content here, making it look like readable English. Many desktop publishing packages and web page editors now use Lorem Ipsum.</p>
    <span class="btn">Read More</span>
  </div>
</section>

<section class="features">
  <div class="wrap">
    <h2 class="section-title">OUR NEW FEATURES</h2>
    <p class="section-sub">Contrary to popular Lorem Ipsum is not simply text.</p>
    <div class="feature-grid">
      <div class="feature">
        <div class="feature-icon"><svg width="26" height="26" viewBox="0 0 26 26" fill="none" stroke="#333" stroke-width="1.5"><circle cx="13" cy="13" r="10"/><path d="M3 13h20M13 3c4 4 4 16 0 20M13 3c-4 4-4 16 0 20"/></svg></div>
        <div><h4>NEQUE PORRO QUISQUAM EST</h4><p>There are many variations of passages of Lorem Ipsum available, but the majority have suffered alteration in some form, by injected humour, or randomised words which don't look.</p><a>READ MORE</a></div>
      </div>
      <div class="feature">
        <div class="feature-icon"><svg width="26" height="26" viewBox="0 0 26 26" fill="none" stroke="#333" stroke-width="1.5"><circle cx="13" cy="13" r="10"/><path d="M17 9l-2 6-6 2 2-6z"/></svg></div>
        <div><h4>NEQUE PORRO QUISQUAM EST</h4><p>There are many variations of passages of Lorem Ipsum available, but the majority have suffered alteration in some form, by injected humour, or randomised words which don't look.</p><a>READ MORE</a></div>
      </div>
      <div class="feature">
        <div class="feature-icon"><svg width="26" height="26" viewBox="0 0 26 26" fill="#333"><path d="M13 3l4 4-4 4-4-4zM7 9l4 4-4 4-4-4zM19 9l4 4-4 4-4-4zM13 15l4 4-4 4-4-4z"/></svg></div>
        <div><h4>NEQUE PORRO QUISQUAM EST</h4><p>There are many variations of passages of Lorem Ipsum available, but the majority have suffered alteration in some form, by injected humour, or randomised words which don't look.</p><a>READ MORE</a></div>
      </div>
      <div class="feature">
        <div class="feature-icon"><svg width="26" height="26" viewBox="0 0 26 26" fill="none" stroke="#333" stroke-width="1.5"><rect x="8" y="3" width="11" height="20" rx="2"/><path d="M12 19h3"/></svg></div>
        <div><h4>NEQUE PORRO QUISQUAM EST</h4><p>There are many variations of passages of Lorem Ipsum available, but the majority have suffered alteration in some form, by injected humour, or randomised words which don't look.</p><a>READ MORE</a></div>
      </div>
    </div>
  </div>

  <div class="stats">
    <div class="stats-col">
      <div class="stat"><div class="stat-icon"><svg width="26" height="22" viewBox="0 0 26 22" fill="none" stroke="#fff" stroke-width="1.5"><rect x="2" y="2" width="22" height="14"/><path d="M9 20h8M13 16v4"/></svg></div><div><b>100+</b><span>Technology</span></div></div>
      <div class="stat"><div class="stat-icon"><svg width="24" height="24" viewBox="0 0 24 24" fill="none" stroke="#fff" stroke-width="1.5"><circle cx="12" cy="8" r="4"/><path d="M4 22c0-5 4-8 8-8s8 3 8 8"/></svg></div><div><b>65+</b><span>Research</span></div></div>
    </div>
    <div class="video-col">
      <div class="play"><svg width="22" height="24" viewBox="0 0 22 24"><path d="M4 2l16 10-16 10z" fill="#fff"/></svg></div>
      <h3>OUR VIDEO</h3>
      <p>Our goal is to provide next generation technology</p>
    </div>
    <div class="stats-col">
      <div class="stat right"><div><b>75+</b><span>Members</span></div><div class="stat-icon"><svg width="28" height="22" viewBox="0 0 28 22" fill="none" stroke="#fff" stroke-width="1.5"><path d="M2 8l12-6 12 6-12 6zM7 11v6c4 3 10 3 14 0v-6"/></svg></div></div>
      <div class="stat right"><div><b>85+</b><span>Countries</span></div><div class="stat-icon"><svg width="22" height="24" viewBox="0 0 22 24" fill="#fff"><path d="M4 2h2v21H4zM6 3h13l-3 5 3 5H6z"/></svg></div></div>
    </div>
  </div>
</section>

<section class="projects">
  <div class="wrap">
    <h2 class="section-title">OUR RECENT <span>PROJECTS</span></h2>
    <div class="project-grid">
      <div class="project"><div class="project-thumb" role="img" aria-label="Photo of a desk with a laptop and a world map" style="background:linear-gradient(135deg,#6e5a4a,#3a6fb0)"></div><p>There are many variations of passages</p></div>
      <div class="project"><div class="project-thumb" role="img" aria-label="Photo of a person relaxing on a beach at sunset" style="background:linear-gradient(180deg,#f0b070,#8aa6c0)"></div><p>But I must explain to you how all this mistaken</p></div>
      <div class="project"><div class="project-thumb" role="img" aria-label="Photo of a laptop and camera on a table" style="background:linear-gradient(135deg,#d9d6d0,#8a8580)"></div><p>There are many variations of passages</p></div>
      <div class="project project-feature">
        <div class="project-thumb" role="img" aria-label="Photo of a city skyline with a clock tower at dusk" style="background:linear-gradient(180deg,#2a4a8a,#c07a5a)"></div>
        <div class="date">11:59 | March 2014</div>
        <h4>Sed ut perspiciatis unde omnis ist natus error sit voluptatem</h4>
        <p>But I must explain to you how all this mistaken idea of denouncing pleasure and praising pain was born and I will give you a complete account of the system, and expound the actual teachings of the great explorer of the truth, the master-builder</p>
      </div>
      <div class="project"><div class="project-thumb" role="img" aria-label="Photo of friends taking a selfie outdoors" style="background:linear-gradient(135deg,#e0a060,#c04a5a)"></div><p>But I must explain to you how all this mistaken</p></div>
      <div class="project"><div class="project-thumb" role="img" aria-label="Photo of a traveller with a suitcase in a terminal" style="background:linear-gradient(135deg,#c8c8c8,#7a7a7a)"></div><p>There are many variations of passages</p></div>
      <div class="project"><div class="project-thumb" role="img" aria-label="Photo of a business person at a desk with a laptop" style="background:linear-gradient(135deg,#3a3a40,#9aa0aa)"></div><p>But I must explain to you how all this mistaken</p></div>
    </div>
  </div>
</section>

<section class="testimonials">
  <div class="wrap">
    <div class="testi-head"><h2>WHAT CLIENT <span>SAYS ABOUT US</span></h2><div class="testi-nav"><i></i><i></i></div></div>
    <div class="testi-label">Client Testimonial</div>
    <div class="testi-grid">
      <div class="testi">
        <div class="testi-top"><div class="avatar" role="img" aria-label="Client portrait"></div><div><b>De Finibus Bonorum</b><span>Course On Java script</span></div></div>
        <p>Contrary to popular belief, Lorem Ipsum is not simply random text. It has roots in a piece of classical Latin literature from 45 BC, making it over 2000 years old. Hollis Ward, a Latin professor at Ashford Hill College in Vermont</p>
      </div>
      <div class="testi">
        <div class="testi-top"><div class="avatar" role="img" aria-label="Client portrait"></div><div><b>De Finibus Bonorum</b><span>Course On Java script</span></div></div>
        <p>Contrary to popular belief, Lorem Ipsum is not simply random text. It has roots in a piece of classical Latin literature from 45 BC, making it over 2000 years old. Hollis Ward, a Latin professor at Ashford Hill College in Vermont</p>
      </div>
    </div>
  </div>
</section>

<section class="blog">
  <div class="wrap">
    <h2 class="section-title">Our Blog Post</h2>
    <p class="section-sub">It is a long established fact a reader will be distracted</p>
    <div class="blog-grid">
      <article class="post"><div class="post-thumb" role="img" aria-label="Photo of a team meeting in an office" style="background:linear-gradient(135deg,#dfe6ee,#7f9ab8)"></div><h4>Job Opportunities</h4><p>Founded in Summit Business Group (SBG) quickly gained</p></article>
      <article class="post"><div class="post-thumb" role="img" aria-label="Photo of colleagues working at a table" style="background:linear-gradient(135deg,#4a6aa0,#c9d6e6)"></div><h4>Professional Services</h4><p>Founded in Summit Business Group (SBG) quickly gained</p></article>
      <article class="post"><div class="post-thumb" role="img" aria-label="Photo of a laptop on a dark desk" style="background:linear-gradient(135deg,#2a2e38,#7a8290)"></div><h4>Career Advice</h4><p>Founded in Summit Business Group (SBG) quickly gained</p></article>
      <article class="post"><div class="post-thumb" role="img" aria-label="Photo of a mountain landscape" style="background:linear-gradient(180deg,#b9c9d6,#7a8a5a)"></div><h4>Resources</h4><p>Founded in Summit Business Group (SBG) quickly gained</p></article>
    </div>
  </div>
</section>

<section class="contact">
  <div class="wrap">
    <h2 class="section-title">Contact us</h2>
    <p class="section-sub">Lorem ipsum dolor sit amet, consectetuer adipiscing elit, sed diam nonummy nibh euismod tincidunt ut laoreet dolore magna aliquam erat volutpat.</p>
    <div class="contact-body">
      <div class="contact-info">
        <h4>Contact Information</h4>
        <ul>
          <li><svg width="12" height="14" viewBox="0 0 12 14" fill="#c9d2ea"><path d="M6 0a5 5 0 015 5c0 4-5 9-5 9S1 9 1 5a5 5 0 015-5zm0 3a2 2 0 100 4 2 2 0 000-4z"/></svg>4821 Orchard Lane, North Ridgeway</li>
          <li><svg width="12" height="12" viewBox="0 0 12 12" fill="#c9d2ea"><path d="M2 0l2 3-1 1.5c1 2 2.5 3.5 4.5 4.5L9 8l3 2-1 2C5 12 0 7 0 1z"/></svg>Phone - (555) 014-2290</li>
          <li><svg width="12" height="12" viewBox="0 0 12 12" fill="#c9d2ea"><rect x="0" y="3" width="12" height="7"/><rect x="3" y="0" width="6" height="3"/></svg>Fax - (555) 014-2291</li>
          <li><svg width="12" height="10" viewBox="0 0 12 10" fill="none" stroke="#c9d2ea"><rect x=".5" y=".5" width="11" height="9"/><path d="M.5 .5l5.5 5 5.5-5"/></svg>E-mail - hello@wayfront.test</li>
        </ul>
        <div class="socials"><i></i><i></i><i></i><i></i><i></i><i></i></div>
      </div>
      <form class="contact-form">
        <div class="form-row"><div class="field">Name</div><div class="field">Mail Id</div></div>
        <div class="field message">Message</div>
        <span class="submit">Submit Now</span>
      </form>
    </div>
  </div>
</section>

<footer class="site-footer">Copyright 2016 © Wayfront Technologies All Rights Reserved.</footer>

</body>
</html>
```